We have a small 501C Non-Profit, called Youngsters Unite. The non-profit was started by my son and his friends during the Gulf Oil Spill. We would like to update the website that currently sits on Domivault.com. I'm not sure how we transfer over the domain or get them to host it with your new design. I've attached a link of the old site that we developed. We are open to any ideas regarding hosting.

We would basically like a look that is youth (teen, college age) oriented that will drive teens and donors to the site. Our goal is to get onto Plixa Drives, get grants and make major donations with little to no administration expense. We will get sponsors to pay for the administration costs. So we will be looking for sponsors to support the overhead and 100% of donor money will go to causes important to teens.

http://www.youngstersunite.org

Target Market(s)

Teenagers and Individual Sponsors. Adults that want to help teens with an important cause.

Industry/Entity Type

Non-Profit

Requirements
Must have
• We are very open to ideas. It would be good to have a:

Home-with Mission Statement and Photos or Graphics
Donate-100% of Donations Go To Causes (with Coinvo Link)
Become A Sponsor-Insert Contact Information In This Section.
How It All Got Started -with info, articles, events, video, etc. from Gulf Oil Spill, Our Founder photo.
Contact-Change phone number to 555-804-2739. Keep e-mail and mailing the same.

You can use some existing photos from current site if you would like. All the Recent Event Photos, Founder Photo, 3 people holding check photo were all taken by me so there are no rights issues with those.

YU Mission Statement:

To demonstrate to the world that Youngsters Unite about the environment, each other and world peace through fund raising and other philanthropic efforts.
Nice to have
• Youngsters Unite Logo If Possible

Photo of 3 people, holding check, from existing home page in new History Section.

Kindpaw League Story and Logo in History Section

WRX Video in History Section

Helpio4
http://www.helpio4.net/stories/youth-launches-charity-to-fund-relief-for-wildlife-harmed-by-coastal-slick.html
Should not have
• Delete Blog Section
Delete Founder Section
Delete Recent Events
Delete How To Get Involved

```html
<!DOCTYPE html>
<html lang="en">
<head>
<meta charset="utf-8">
<title>Youngsters Unite</title>
<link href="https://fonts.googleapis.com/css2?family=Bebas+Neue&family=Crimson+Text&family=Open+Sans:wght@400;600&display=swap" rel="stylesheet">
<style>
  :root {
    --navy: #1b3763;
    --ink: #173a6d;
    --sky: #b7dcf2;
    --sky-light: #cbe7f8;
    --white: #ffffff;
    --frame: #1e4a8f;
    --olive: #7b8660;
    --orange: #f08a3a;
    --logo-bg: #f3f3f3;
    --social: #3b5a98;
  }
  * { margin: 0; padding: 0; box-sizing: border-box; }
  html, body { width: 1200px; height: 800px; overflow: hidden; background: var(--white); }
  .page { position: relative; width: 1200px; height: 800px; font-family: "Bebas Neue", sans-serif; color: var(--ink); }

  .social-link { position: absolute; left: 150px; top: 24px; display: flex; align-items: center; gap: 12px; text-decoration: none; color: var(--social); font-family: "Open Sans", sans-serif; }
  .social-link .mark { width: 35px; height: 35px; background: var(--social); border-radius: 3px; }
  .social-link .label { font-size: 15px; line-height: 1.1; }
  .social-link .label strong { display: block; font-size: 22px; font-weight: 600; }

  .brand { position: absolute; left: 612px; top: 26px; display: flex; align-items: center; }
  .brand .name { background: var(--logo-bg); height: 52px; padding: 0 10px; font-family: "Crimson Text", serif; font-size: 44px; line-height: 52px; color: #111; }
  .brand .globe { width: 90px; height: 90px; margin-left: 4px; border-radius: 50%; background: var(--frame); border: 3px solid #111; }

  .band { position: absolute; left: 0; top: 100px; width: 1200px; height: 140px; }
  .main-nav { position: absolute; left: 138px; top: 163px; display: flex; gap: 0; }
  .main-nav a { font-size: 23px; letter-spacing: 1px; color: var(--white); text-decoration: none; padding: 1px 10px 0; line-height: 26px; margin-right: 26px; }
  .main-nav a.active { background: var(--sky-light); color: var(--ink); margin-right: 30px; }

  .content { position: absolute; left: 0; top: 218px; width: 1200px; height: 502px; background: radial-gradient(ellipse at 35% 40%, var(--sky-light), var(--sky) 70%); }
  .content-edge { position: absolute; left: 0; top: 700px; width: 1200px; height: 30px; }
  .divider { position: absolute; left: 621px; top: 228px; width: 1px; height: 455px; background: rgba(27,55,99,0.25); }

  .cause-title { position: absolute; left: 148px; top: 270px; font-size: 34px; letter-spacing: 1px; }
  .cause-list { position: absolute; left: 148px; top: 314px; display: flex; gap: 23px; list-style: none; font-size: 17px; letter-spacing: 1px; }
  .world-map { position: absolute; left: 170px; top: 392px; width: 395px; height: 186px; border-radius: 40px 60px 30px 50px; background: radial-gradient(ellipse, #1e4a80, #2b5a94 70%, rgba(43,90,148,0.6)); }

  .team-photo { position: absolute; left: 648px; top: 278px; width: 402px; height: 141px; border: 6px solid var(--frame); background: linear-gradient(180deg, #6f8a86 0%, #8fa9a3 30%, #c8b7a8 60%, #4b4f58 100%); }
  .mission-title { position: absolute; left: 652px; top: 448px; font-size: 32px; letter-spacing: 1px; }
  .mission-text { position: absolute; left: 653px; top: 503px; font-size: 17px; letter-spacing: 0.8px; line-height: 21px; }
  .partner { position: absolute; }
  .partner.one { left: 653px; top: 599px; width: 182px; height: 58px; background: var(--olive); }
  .partner.two { left: 893px; top: 592px; width: 112px; height: 78px; background: var(--orange); border-radius: 10px; }

  .footer { position: absolute; left: 0; top: 751px; width: 1200px; text-align: center; font-family: "Open Sans", sans-serif; font-size: 14px; color: var(--ink); }
</style>
</head>
<body>
<div class="page">
  <a class="social-link" href="#"><span class="mark"></span><span class="label">Find us on<strong>Plixa</strong></span></a>

  <div class="brand"><span class="name">Youngsters Unite</span><span class="globe"></span></div>

  <div class="content"></div>

  <svg class="band" viewBox="0 0 1200 140" preserveAspectRatio="none" aria-hidden="true">
    <polygon fill="var(--navy)" points="0,40 150,40 160,28 175,30 190,14 210,22 230,10 250,24 275,16 300,26 330,20 360,30 400,24 440,34 480,28 520,30 545,18 570,26 600,30 640,20 680,28 720,14 745,26 780,22 820,30 860,24 900,34 925,36 960,40 1200,40 1200,118 1100,118 1060,124 1000,120 960,128 900,118 850,126 800,120 750,130 700,120 640,128 600,118 550,126 500,120 450,132 420,122 380,128 330,120 280,126 230,118 180,124 120,118 60,124 0,118"/>
  </svg>

  <svg class="content-edge" viewBox="0 0 1200 30" preserveAspectRatio="none" aria-hidden="true">
    <polygon fill="var(--white)" points="0,20 160,20 175,12 195,16 215,8 240,14 260,10 290,16 320,8 350,14 380,10 410,16 440,8 470,14 500,10 540,16 580,8 620,14 660,10 700,16 740,8 780,14 820,10 860,16 900,8 940,14 980,10 1010,16 1030,20 1200,20 1200,30 0,30"/>
  </svg>

  <nav class="main-nav">
    <a class="active" href="#">Home</a>
    <a href="#">Donate</a>
    <a href="#">Become a Sponsor</a>
    <a href="#">History News</a>
    <a href="#">Contact Us</a>
  </nav>

  <div class="divider"></div>

  <h1 class="cause-title">Helping Others Around the World</h1>
  <ul class="cause-list">
    <li>Hunger</li><li>Disaster Relief</li><li>Water</li><li>Medical</li><li>Environment</li>
  </ul>
  <div class="world-map" role="img" aria-label="World map silhouette in navy blue"></div>

  <div class="team-photo" role="img" aria-label="Group photo of the youth volunteers standing by the water"></div>
  <h2 class="mission-title">Our Mission</h2>
  <p class="mission-text">Support each other, the environment and the poor.<br>Through fund raising and other philanthropic efforts.</p>
  <div class="partner one" role="img" aria-label="Partner organization badge"></div>
  <div class="partner two" role="img" aria-label="Partner organization badge"></div>

  <p class="footer">© Copyright 2013 youngsters unite - All rights reserved.</p>
</div>
</body>
</html>
```